KQW Authorised Dealer needs Business Cards

We need a business card designed for our branch owners. Vellmor Alarms is an Authorised KQW Dealer and does its own independent installations outside of the KQW work we perform so whilst the KQW Authorised Dealer Logo needs to be included, it should not be overwhelming in respect of the overall look of the card. I would like a rounded edge to the cards corners rather than a 90 degree hard edge. We also need to promote the fact that we do First Class Alarm & CCTV Solutions. (Details of card holder to follow)

```html
<!DOCTYPE html>
<html lang="en">
<head>
<meta charset="utf-8">
<title>Vellmor Alarms – Business Card</title>
<link rel="stylesheet" href="https://fonts.googleapis.com/css2?family=Oswald:wght@500&family=Cinzel:wght@400&family=Questrial&display=swap">
<style>
  :root {
    --backdrop: #1d1d1f;
    --card-white: #ffffff;
    --card-mist: #e4e6e9;
    --brand-blue: #1f7cc4;
    --brand-blue-deep: #0f5d9e;
    --slate: #4a4c50;
    --slate-light: #8d9096;
    --ink: #2a2b2e;
    --faint-blue: #c9dcec;
    --faint-grey: #c4c6ca;
  }
  * { box-sizing: border-box; margin: 0; padding: 0; }
  html, body {
    width: 1200px; height: 871px; overflow: hidden;
    background: var(--backdrop);
  }
  .sheet {
    position: relative; width: 1200px; height: 871px;
    display: flex; flex-direction: column; align-items: center;
    justify-content: center; gap: 37px;
  }
  .card {
    position: relative; width: 660px; height: 377px;
    border-radius: 30px; overflow: hidden;
    background: linear-gradient(160deg, var(--card-white) 0%, var(--card-white) 45%, var(--card-mist) 100%);
    box-shadow: 0 10px 28px rgba(0,0,0,.5);
  }
  .card__waves { position: absolute; inset: 0; width: 100%; height: 100%; }

  /* back */
  .brand-lockup {
    position: absolute; left: 100px; top: 110px;
    display: flex; align-items: center; gap: 16px;
  }
  .brand-lockup__dot {
    width: 34px; height: 34px; background: var(--brand-blue); border-radius: 4px;
  }
  .brand-lockup__name {
    font-family: 'Oswald', sans-serif; font-weight: 500;
    font-size: 50px; line-height: 1.2; letter-spacing: 1px; color: var(--slate);
    text-transform: uppercase;
  }
  .tagline {
    position: absolute; left: 150px; top: 192px;
    font-family: 'Questrial', sans-serif; font-size: 14px;
    letter-spacing: 2.5px; color: var(--brand-blue); text-transform: uppercase;
  }
  .partner-mark {
    position: absolute; right: 120px; top: 78px;
    display: flex; align-items: center; gap: 8px;
  }
  .partner-mark__circle {
    width: 30px; height: 30px; border-radius: 50%; background: var(--brand-blue-deep);
  }
  .partner-mark__name {
    font-family: 'Oswald', sans-serif; font-weight: 500;
    font-size: 22px; color: var(--brand-blue-deep);
  }

  /* front */
  .front__wordmark {
    position: absolute; left: 60px; top: 34px;
    font-family: 'Oswald', sans-serif; font-weight: 500;
    font-size: 38px; line-height: 1.2; letter-spacing: 1px; color: var(--slate);
    text-transform: uppercase;
  }
  .front__emblem {
    position: absolute; right: 20px; top: 110px; width: 210px; height: 250px;
    border-radius: 8px 8px 0 0;
    background: linear-gradient(180deg, var(--faint-blue) 0%, var(--faint-grey) 60%, rgba(196,198,202,.4) 100%);
    opacity: .65;
  }
  .holder {
    position: absolute; left: 55px; top: 128px;
  }
  .holder__name {
    font-family: 'Cinzel', serif; font-size: 17px; letter-spacing: 1.5px; color: var(--ink);
  }
  .holder__role {
    font-family: 'Cinzel', serif; font-size: 11px; letter-spacing: 2px;
    color: var(--brand-blue); margin-top: 1px; text-transform: uppercase;
  }
  .contact {
    position: absolute; left: 300px; top: 172px; list-style: none;
    font-family: 'Questrial', sans-serif; font-size: 13.5px; letter-spacing: 1.8px;
    color: var(--ink); line-height: 1.45;
  }
  .contact__address { margin-bottom: 8px; }
  .contact__item { display: flex; align-items: center; gap: 14px; margin-bottom: 3px; }
  .contact__icon { width: 13px; height: 13px; flex: none; fill: var(--brand-blue); margin-left: -27px; }
</style>
</head>
<body>
<main class="sheet">

  <section class="card card--back" aria-label="Card back">
    <svg class="card__waves" viewBox="0 0 660 377" preserveAspectRatio="none" aria-hidden="true">
      <path d="M0,250 C180,300 420,320 660,282 L660,377 L0,377 Z" fill="#bfc1c5"/>
      <path d="M0,262 C180,312 420,332 660,294 L660,377 L0,377 Z" fill="#55575b"/>
      <path d="M0,278 C190,328 430,346 660,308 L660,377 L0,377 Z" fill="#ffffff"/>
      <path d="M0,290 C190,338 430,356 660,318 L660,377 L0,377 Z" fill="var(--brand-blue)"/>
    </svg>
    <div class="brand-lockup">
      <span class="brand-lockup__dot"></span>
      <span class="brand-lockup__name">Vellmor Alarms</span>
    </div>
    <p class="tagline">First Class Alarm &amp; CCTV Solutions</p>
    <div class="partner-mark">
      <span class="partner-mark__circle"></span>
      <span class="partner-mark__name">KQW</span>
    </div>
  </section>

  <section class="card card--front" aria-label="Card front">
    <div class="front__emblem" role="img" aria-label="Faint large company emblem in pale blue and grey"></div>
    <svg class="card__waves" viewBox="0 0 660 377" preserveAspectRatio="none" aria-hidden="true">
      <path d="M0,190 C110,200 230,300 400,320 C500,332 590,325 660,322 L660,377 L0,377 Z" fill="#c7c9cd"/>
      <path d="M0,204 C110,214 230,312 400,332 C500,344 590,337 660,334 L660,377 L0,377 Z" fill="#55575b"/>
      <path d="M0,216 C110,226 230,322 400,342 C500,352 590,346 660,343 L660,377 L0,377 Z" fill="#ffffff"/>
      <path d="M0,228 C110,238 230,332 400,352 C500,362 590,356 660,352 L660,377 L0,377 Z" fill="var(--brand-blue)"/>
    </svg>
    <div class="front__wordmark">Vellmor Alarms</div>
    <div class="holder">
      <p class="holder__name">Elena Varga</p>
      <p class="holder__role">President</p>
    </div>
    <ul class="contact">
      <li class="contact__address">24 Mill Lane, Suite 300 Harlow<br>MA 02190</li>
      <li class="contact__item">
        <svg class="contact__icon" viewBox="0 0 16 16" aria-hidden="true"><path d="M1 5c0-2 2-3 7-3s7 1 7 3v1h-4V5H5v1H1zM3 8h10l1 6H2z"/></svg>
        555.204.1187
      </li>
      <li class="contact__item">
        <svg class="contact__icon" viewBox="0 0 16 16" aria-hidden="true"><path d="M4 1h8v14H4zM5.5 3v9h5V3z"/></svg>
        555.318.4420
      </li>
      <li class="contact__item">
        <svg class="contact__icon" viewBox="0 0 16 16" aria-hidden="true"><path d="M1 3h14v10H1zM2.5 4.5 8 9l5.5-4.5z"/></svg>
        varga@vellmoralarms.com
      </li>
    </ul>
  </section>

</main>
</body>
</html>
```